information security company tri-fold brochure

Attached is our existing tri-fold PDF and our new logo. We need something that uses the new logo and appropriate color. The wording we will change up a bit, but the existing brochure gives you an idea what it will be like. our customers are banks, finance companies and health care entities so the design should have those sorts of folks in mind.

Security

```html
<!DOCTYPE html>
<html lang="en">
<head>
<meta charset="utf-8">
<title>Calverton Group – Tri-fold Brochure</title>
<link rel="stylesheet" href="https://fonts.googleapis.com/css2?family=Ubuntu:wght@300;400;500&display=swap">
<style>
  :root {
    --brand-blue: #2e3192;
    --stage-grey: #7a7a7a;
    --panel-grey: #c6c7c9;
    --header-grey: #c9cacc;
    --ink: #3f3f3f;
    --ink-dark: #333333;
    --paper: #ffffff;
  }
  * { margin: 0; padding: 0; box-sizing: border-box; }
  html, body { width: 1200px; height: 900px; overflow: hidden; }
  body {
    background: var(--stage-grey);
    font-family: "Ubuntu", sans-serif;
    color: var(--ink);
    position: relative;
  }
  .brochure {
    position: absolute; left: 70px; top: 69px;
    width: 1066px; height: 758px;
    background: var(--paper);
    overflow: hidden;
  }
  .abs { position: absolute; }

  /* structure */
  .top-band { left: 322px; top: 0; width: 744px; height: 70px; background: var(--brand-blue); }
  .fold { top: 0; height: 758px; border-left: 1px dashed #555; }
  .fold--one { left: 350px; }
  .fold--two { left: 705px; }
  .side-column { left: 656px; top: 116px; width: 139px; height: 642px; background: var(--panel-grey); }

  /* left panel */
  .brand-mark { left: 40px; top: 14px; display: flex; align-items: center; gap: 8px; }
  .brand-mark .dot { width: 22px; height: 22px; border-radius: 50%; background: var(--brand-blue); }
  .brand-mark span { font-size: 15px; font-weight: 500; color: var(--brand-blue); }
  .headline-bar { left: 0; top: 70px; width: 322px; height: 61px; background: var(--header-grey); }
  .headline-bar h2 { position: absolute; left: 39px; top: 17px; font-size: 21px; font-weight: 500; color: var(--brand-blue); }
  .intro { left: 39px; top: 140px; font-size: 12px; line-height: 17px; }
  .pie { left: 0; top: 0; }
  .stat { color: #fff; font-weight: 500; line-height: 1; }
  .stat--70 { left: 114px; top: 253px; font-size: 40px; }
  .stat--note { left: 104px; top: 306px; font-size: 14px; font-weight: 300; }
  .stat--30 { left: 101px; top: 325px; font-size: 40px; }
  .stat-caption { font-size: 11.5px; line-height: 14px; font-weight: 500; }
  .stat-caption--blue { left: 200px; top: 250px; color: var(--brand-blue); }
  .stat-caption--dark { left: 183px; top: 343px; color: var(--ink-dark); font-size: 13px; line-height: 16px; }
  .warning { left: 39px; top: 412px; font-size: 12px; line-height: 17px; }
  .contact-bar { left: 0; top: 450px; width: 145px; height: 26px; background: var(--brand-blue); color: #fff; font-size: 19px; padding-left: 40px; line-height: 26px; }
  .contact-copy { left: 40px; top: 481px; width: 104px; font-size: 11px; line-height: 17.3px; letter-spacing: -0.3px; }
  .photo--worried { left: 146px; top: 476px; width: 202px; height: 282px; background: linear-gradient(180deg, #eef0f4 0%, #b9cbe3 55%, #2a2a2e 100%); }
  .quote-rule { left: 40px; top: 641px; width: 138px; border-top: 1px solid var(--brand-blue); }
  .quote { left: 177px; top: 638px; font-size: 12.5px; line-height: 16.5px; color: var(--brand-blue); }

  /* middle panel */
  .photo--office { left: 375px; top: 42px; width: 81px; height: 161px; background: linear-gradient(180deg, #cfd8e0, #5e6770 70%, #2b2f33); }
  .photo--clinic { left: 468px; top: 42px; width: 76px; height: 161px; background: linear-gradient(180deg, #67b59a, #5d86b8 55%, #24385a); }
  .photo--case { left: 556px; top: 42px; width: 78px; height: 161px; background: linear-gradient(180deg, #5f6570, #9a9ca0 50%, #3b3d40); }
  .brand-small { left: 377px; top: 583px; display: flex; align-items: center; gap: 7px; }
  .brand-small .dot { width: 18px; height: 18px; border-radius: 50%; background: var(--brand-blue); }
  .brand-small span { font-size: 13px; font-weight: 500; color: var(--brand-blue); }
  .address { left: 434px; top: 623px; font-size: 11.5px; line-height: 17.5px; }

  /* right panel */
  .company-line { left: 852px; top: 48px; font-size: 11px; font-weight: 500; color: #fff; }
  .logo-disc { left: 728px; top: 41px; width: 124px; height: 124px; border-radius: 50%; background: var(--paper); }
  .brand-large { left: 755px; top: 92px; font-size: 19px; font-weight: 500; color: var(--brand-blue); white-space: nowrap; }
  .tagline { left: 853px; top: 220px; font-size: 19px; font-weight: 300; line-height: 21px; }
  .tagline .highlight { display: block; background: var(--brand-blue); color: #fff; width: 215px; margin: 3px 0 3px -2px; padding: 1px 0 1px 6px; font-weight: 400; }
  .photo--seated { left: 810px; top: 400px; width: 230px; height: 290px; background: linear-gradient(180deg, #f2f2f2 0%, #c9b7e6 40%, #2a2a2e 75%, #ffffff 100%); border-radius: 40% 40% 10% 10%; }
  .side-title {
    left: 748px; top: 688px;
    transform: rotate(-90deg); transform-origin: 0 0;
    font-size: 39px; line-height: 44px; font-weight: 300;
    color: #fff; white-space: nowrap; letter-spacing: 0.6px;
  }
</style>
</head>
<body>
<main class="brochure">
  <div class="abs top-band"></div>
  <div class="abs side-column"></div>

  <!-- left panel -->
  <div class="abs brand-mark"><i class="dot"></i><span>Calverton Group</span></div>
  <div class="abs headline-bar"><h2>Just a phone call away...</h2></div>
  <p class="abs intro">The Calverton Group is the premier Midwest<br>security services firm.</p>

  <svg class="abs pie" width="350" height="460" viewBox="0 0 350 460" aria-hidden="true">
    <path d="M115 293 L199 293 A84 84 0 0 1 66.8 361.8 Z" fill="var(--ink-dark)"/>
    <path d="M115 293 L66.8 361.8 A84 84 0 1 1 199 293 Z" fill="var(--brand-blue)"/>
    <line x1="115" y1="293" x2="66.8" y2="361.8" stroke="#fff" stroke-width="4"/>
    <line x1="115" y1="293" x2="199" y2="293" stroke="#fff" stroke-width="3"/>
  </svg>
  <div class="abs stat stat--70">70%</div>
  <p class="abs stat-caption stat-caption--blue">of all companies<br>have a security breach<br>of some sort</p>
  <div class="abs stat stat--note">while only</div>
  <div class="abs stat stat--30">30%</div>
  <p class="abs stat-caption stat-caption--dark">of those even<br>know it!</p>

  <p class="abs warning">Don't let your organization<br>be caught off guard.</p>
  <div class="abs contact-bar">contact us</div>
  <div class="abs photo--worried" role="img" aria-label="Photo of a stressed businessman in a blue shirt holding his head"></div>
  <p class="abs contact-copy">Contact<br>The Calverton Group<br>today.<br>Our services<br>are both affordable<br>&nbsp;and extremely<br>valuable<br>to organizations<br>&nbsp;of all types.</p>
  <div class="abs quote-rule"></div>
  <p class="abs quote">What you don't know<br>is more dangerous<br>than you might think....</p>

  <div class="abs fold fold--one"></div>
  <div class="abs fold fold--two"></div>

  <!-- middle panel -->
  <div class="abs photo--office" role="img" aria-label="Photo of a businessman on the phone at an office desk"></div>
  <div class="abs photo--clinic" role="img" aria-label="Photo of a surgeon in cap and mask"></div>
  <div class="abs photo--case" role="img" aria-label="Photo of a person in a suit carrying a briefcase"></div>
  <div class="abs brand-small"><i class="dot"></i><span>Calverton Group</span></div>
  <p class="abs address">PO BOX 51827<br>Lakemont, IN 46999<br>Daniel Ferro<br>Account Manager<br>Phone: (555) 014-2207<br>E-mail: daniel@calverton-group.example</p>

  <!-- right panel -->
  <div class="abs company-line">The Calverton Group, Inc.</div>
  <div class="abs logo-disc"></div>
  <div class="abs brand-large">Calverton Group</div>
  <p class="abs tagline">Committed<span class="highlight">to protecting</span>your business<br>and your bottom line.</p>
  <div class="abs photo--seated" role="img" aria-label="Photo of a seated businessman holding a sheet with a folder and key sketch in front of his face"></div>
  <div class="abs side-title">Is your information safe?</div>
</main>
</body>
</html>
```